"Breakthrough! Mapping the Coastal Escape" NEEDS BOOK COVER!

Hello - please see the attached BOOK COVER DESIGN BRIEF document for full instructions and content required for cover.

I am really seeking clean, professional designs here that follow my instructions. The cover MUST jump out in a thumbnail (as if on Brindlow) - any covers that are too busy, messy or unprofessional will be eliminated.

Any questions please ask.

Thanks.
Colin
Updates

Project Deadline Extended
Reason: This project has been extended to invite more designers, as I haven't received enough options to choose from. Hoping this extra few days allows a few more submissions. Thank you to existing designers for your submissions, a number of them are in the running.

Target Market(s)

Please see the attached brief for full instructions on this project.

Industry/Entity Type

Property

Font styles to use
Serif
Sans Serif

Requirements
Must have
• Please see the attached brief for full instructions on this project.
Nice to have
Should not have

```html
<!DOCTYPE html>
<html lang="en">
<head>
<meta charset="utf-8">
<title>Breakthrough! Mapping the Coastal Escape – Book Cover</title>
<link href="https://fonts.googleapis.com/css2?family=Open+Sans:wght@400;600;700;800&family=Oswald:wght@700&display=swap" rel="stylesheet">
<style>
  :root {
    --red: #ee2a12;
    --ink: #1c1c1c;
    --navy: #23265e;
    --paper: #d9d9d9;
    --paper-light: #e6e6e6;
    --page: #ffffff;
    --white: #ffffff;
  }
  * { box-sizing: border-box; margin: 0; padding: 0; }
  html, body { width: 1200px; height: 857px; overflow: hidden; background: var(--page); }
  body { position: relative; font-family: "Open Sans", Arial, sans-serif; color: var(--ink); }

  .spread {
    position: absolute; left: 53px; top: 52px; width: 1095px; height: 756px;
    background: radial-gradient(ellipse at 75% 40%, var(--paper-light), var(--paper) 70%);
    box-shadow: 0 2px 8px rgba(0,0,0,.3);
    overflow: hidden;
  }
  .abs { position: absolute; }

  /* Back cover */
  .back-kicker { left: 17px; top: 40px; color: var(--red); font-weight: 800; font-size: 25px; }
  .back-title { left: 17px; top: 70px; font-weight: 800; font-size: 26px; line-height: 33px; letter-spacing: .3px; }
  .back-sub { left: 17px; top: 150px; width: 250px; font-size: 14px; line-height: 18px; }
  .back-intro { left: 287px; top: 76px; width: 240px; font-size: 14px; line-height: 19px; }
  .back-intro strong { display: block; font-size: 10px; margin-bottom: 2px; }
  .back-intro em { font-style: italic; }

  .benefits { left: 17px; top: 236px; width: 258px; font-size: 11.8px; line-height: 14.3px; list-style: none; }
  .benefits li { position: relative; padding-left: 12px; margin-bottom: 1px; }
  .benefits li::before { content: "•"; position: absolute; left: 0; }
  .back-body { left: 17px; top: 492px; width: 258px; font-size: 10px; line-height: 13px; }

  .praise-panel {
    left: 277px; top: 228px; width: 258px; height: 386px; background: var(--red);
    color: var(--white); padding: 38px 14px 0 12px; font-size: 11.8px; line-height: 14.4px;
  }
  .praise-panel blockquote { margin-bottom: 22px; }
  .praise-panel cite { display: block; text-align: right; font-style: italic; font-weight: 700; margin-top: 3px; padding-right: 8px; }

  .brand-name { left: 40px; top: 636px; width: 208px; text-align: center; color: var(--navy); font-size: 26px; font-weight: 700; }
  .brand-town { left: 40px; top: 676px; width: 208px; text-align: center; color: var(--navy); font-size: 17px; }
  .brand-url { left: 40px; top: 702px; width: 208px; text-align: center; color: var(--navy); font-size: 11px; font-weight: 700; }

  /* Spine */
  .spine-authors, .spine-title, .spine-brand {
    writing-mode: vertical-rl; white-space: nowrap; font-weight: 700;
  }
  .spine-authors { left: 536px; top: 18px; font-size: 11px; }
  .spine-title { left: 534px; top: 252px; color: var(--red); font-size: 13px; letter-spacing: .6px; }
  .spine-brand { left: 538px; top: 640px; color: var(--navy); font-size: 10px; }

  /* Arrow band across both covers */
  .arrow-band { left: 0; top: 206px; }

  /* Front cover */
  .stamp {
    left: 594px; top: 40px; border: 5px solid var(--red); padding: 6px 14px;
    color: var(--red); font-family: "Oswald", "Arial Narrow", sans-serif; font-size: 30px; line-height: 34px;
    transform: rotate(-7deg); transform-origin: left top;
  }
  .front-authors { left: 836px; top: 114px; font-size: 12px; font-weight: 700; }
  .front-title-main { left: 612px; top: 128px; font-size: 84px; font-weight: 400; letter-spacing: -1px; line-height: 96px; }
  .front-title-link { left: 974px; top: 205px; font-size: 21px; font-weight: 800; line-height: 28px; }
  .front-title-end { left: 614px; top: 228px; font-size: 45px; font-weight: 800; line-height: 60px; letter-spacing: .2px; }
  .front-band {
    left: 562px; top: 301px; width: 533px; height: 86px; background: var(--red); color: var(--white);
    display: flex; align-items: center; justify-content: center; text-align: center;
    font-size: 20px; line-height: 25px; padding: 0 10px;
  }
  .front-band b { font-weight: 700; }

  .cover-art {
    left: 590px; top: 420px; width: 490px; height: 300px;
    background: linear-gradient(180deg, rgba(217,217,217,0) 0%, #cfc6b6 45%, #d8b45a 65%, #e9e6e0 85%, #d5d5d5 100%);
    border-radius: 6px;
  }
</style>
</head>
<body>
  <main class="spread">
    <!-- Back cover -->
    <p class="abs back-kicker">BREAKTHROUGH!</p>
    <h2 class="abs back-title">MAPPING THE<br>COASTAL ESCAPE</h2>
    <p class="abs back-sub">Everything You Didn’t Know About Property And Mortgages, But Wish You Did!</p>
    <p class="abs back-intro"><strong>Daniel Prescott &amp; Dana Gurley</strong><em>Breakthrough! Mapping the Coastal Escape</em> is the smart home buyers guide to mortgages, property, investing and making your dreams reality. This easy to read book will teach you:</p>

    <ul class="abs benefits">
      <li>Five things you must know before buying a property and mortgage – don’t approach any bank or broker before understanding this.</li>
      <li>How to maximise your chances of getting your loan approved – including help on deposit savings and working out how much you can borrow.</li>
      <li>The mortgage and property process explained in six easy steps – with the five stressful mortgage mistakes to avoid.</li>
      <li>Tips to getting smarter with your money and how to pay off your home loan in record time.</li>
      <li>The accidental investor vs. the planned investor – and why most Australians invest for the wrong reasons.</li>
    </ul>
    <p class="abs back-body">The Great Australian Dream of owning your own property, or starting an investment portfolio, can become a great Australian nightmare if you don’t have the right knowledge and team to support you and your dreams.<br>So before taking your next step, read this book carefully and get the insider tips to make confident decisions with your money and your future.</p>

    <section class="abs praise-panel">
      <blockquote>“Daniel professionally guided me through the process of applying for my first home loan. He made what would normally be a worrying task into something enjoyable and stress-free. I found Daniel’s knowledge and confidence in the home loan market impressive. Thank you for helping me make my first big step into a positive future.”<cite>- Alan Ward, QLD</cite></blockquote>
      <blockquote>“I was reluctant in the past to deal with a broker rather than a major bank. Daniel has changed this. He is a totally professional, knowledgeable man – who is genuinely happy to deal with us. He worked hard to make us happy with the best deal possible. His help has turned us from having nothing to being totally financially independent.”<cite>- Keith Rowe, Cairns, QLD</cite></blockquote>
    </section>

    <p class="abs brand-name">HARBOR LEND</p>
    <p class="abs brand-town">Harbor Lend Cairns</p>
    <p class="abs brand-url">WWW.HARBORLENDCAIRNS.COM.AU</p>

    <!-- Spine -->
    <p class="abs spine-authors">Daniel Prescott &amp; Dana Gurley</p>
    <p class="abs spine-title">BREAKTHROUGH! MAPPING THE COASTAL ESCAPE</p>
    <p class="abs spine-brand">HARBOR LEND</p>

    <svg class="abs arrow-band" width="980" height="24" viewBox="0 0 980 24" aria-hidden="true">
      <rect x="0" y="6" width="948" height="12" fill="var(--red)"/>
      <polygon points="942,0 966,12 942,24" fill="var(--red)"/>
    </svg>

    <!-- Front cover -->
    <p class="abs stamp">BREAKTHROUGH</p>
    <p class="abs front-authors">Daniel Prescott &amp; Dana Gurley</p>
    <h1 class="abs front-title-main">MAPPING</h1>
    <p class="abs front-title-link">THE</p>
    <p class="abs front-title-end">COASTAL ESCAPE</p>
    <p class="abs front-band"><span>The Smart Home Buyers <b>Guide To</b><br><b>Mortgages, Property, Investing</b> and<br><b>Making Your Dreams Reality!</b></span></p>

    <div class="abs cover-art" role="img" aria-label="Illustration of three white houses of rising size beside stacks of gold coins, with a red arrow curving upward"></div>
  </main>
</body>
</html>
```